Couples Workshop Flyer

I need a flyer to promote a one-day workshop for couples.

I am a therapist and life-coach and the session is called: "Lantern Bridge Days, and bring out the best in each other' - so Lantern Bridge Days is the bold name for the seminar but the point of the whole workshop is in the tagline, 'and bring out the best in each other'.

The final design should compel couples to take the risk to leave their comfort zones and attend a one-day workshop on a weekend .

Target Market(s)

Couples who are interested in self-improvement and identify with change and growth.
Somehow the flyer will match their aspirations!

Requirements
Should not have
• Not too many love hearts! :)
Not too gushy - a hint of romance!

```html
<!DOCTYPE html>
<html lang="en">
<head>
<meta charset="utf-8">
<title>Lantern Bridge Days – Couples Seminar Flyer</title>
<link rel="stylesheet" href="https://fonts.googleapis.com/css2?family=Carlito:wght@400;700&display=swap">
<style>
  :root {
    --pink: #e8385e;
    --pink-light: #ee5a78;
    --pink-dark: #dc2c53;
    --white: #ffffff;
    --footer: #454343;
    --stripe-blue: #3aa6dc;
    --stripe-yellow: #f4c514;
    --stripe-green: #8cc63e;
    --photo-light: #d9d2b8;
    --photo-mid: #a8a27a;
    --photo-dark: #5d6a3c;
  }
  * { margin: 0; padding: 0; box-sizing: border-box; }
  html, body {
    width: 1200px;
    height: 2749px;
    overflow: hidden;
    background: var(--white);
  }
  .flyer {
    position: relative;
    width: 1200px;
    height: 2749px;
    font-family: "Carlito", "Calibri", sans-serif;
    color: var(--white);
    text-align: center;
    overflow: hidden;
  }
  .facets {
    position: absolute;
    inset: 0;
    width: 100%;
    height: 100%;
  }
  .panel { position: absolute; left: 0; width: 1200px; }

  .header { top: 0; height: 404px; background: var(--pink); overflow: hidden; }
  .header__title {
    position: absolute; left: 0; right: 0; top: 130px;
    font-size: 76px; font-weight: 700; line-height: 1;
  }
  .header__tagline {
    position: absolute; left: 0; right: 0; top: 242px;
    font-size: 37px; line-height: 1;
  }

  .stripe { height: 11px; display: flex; }
  .stripe span { flex: 1; }
  .stripe .blue { background: var(--stripe-blue); }
  .stripe .yellow { background: var(--stripe-yellow); }
  .stripe .green { background: var(--stripe-green); }
  .stripe--top { top: 404px; }
  .stripe--bottom { top: 2440px; }

  .photo {
    top: 415px; height: 845px;
    background:
      radial-gradient(ellipse at 30% 20%, var(--photo-light) 0%, transparent 55%),
      radial-gradient(ellipse at 80% 70%, #efe4c8 0%, transparent 50%),
      linear-gradient(135deg, var(--photo-mid) 0%, var(--photo-dark) 100%);
  }

  .body { top: 1260px; height: 1180px; background: var(--pink); overflow: hidden; }
  .body__intro {
    position: absolute; left: 0; right: 0; top: 88px;
    font-size: 29px; line-height: 42px;
  }
  .body__question {
    position: absolute; left: 0; right: 0; top: 300px;
    font-weight: 700;
  }
  .body__question-lead { display: block; font-size: 76px; line-height: 92px; }
  .body__question-rest { display: block; font-size: 56px; line-height: 70px; }
  .body__pitch {
    position: absolute; left: 0; right: 0; top: 600px;
    font-size: 42px; font-weight: 700; line-height: 62px;
  }
  .presenter {
    position: absolute; left: 0; right: 0; top: 870px;
  }
  .presenter__label { font-size: 34px; line-height: 1; }
  .presenter__name {
    margin-top: 46px;
    font-size: 58px; font-weight: 700; letter-spacing: 4px; line-height: 1;
  }
  .presenter__role { margin-top: 22px; font-size: 24px; line-height: 1; }

  .footer { top: 2451px; height: 298px; background: var(--footer); }
  .footer__cta {
    position: absolute; left: 0; right: 0; top: 108px;
    font-size: 31px; line-height: 1;
  }
  .footer__url {
    position: absolute; left: 0; right: 0; top: 156px;
    font-size: 38px; font-weight: 700; line-height: 1;
  }
</style>
</head>
<body>
<main class="flyer">

  <header class="panel header">
    <svg class="facets" viewBox="0 0 1200 404" preserveAspectRatio="none" aria-hidden="true">
      <polygon points="0,0 420,0 160,404 0,404" fill="var(--pink-light)" opacity="0.35"/>
      <polygon points="780,0 1200,0 1200,300" fill="var(--pink-dark)" opacity="0.45"/>
      <polygon points="500,404 900,120 1200,404" fill="var(--pink-light)" opacity="0.25"/>
    </svg>
    <h1 class="header__title">Lantern Bridge Days</h1>
    <p class="header__tagline">and bring out the best in each other</p>
  </header>

  <div class="panel stripe stripe--top"><span class="blue"></span><span class="yellow"></span><span class="green"></span></div>

  <div class="panel photo" role="img" aria-label="Photograph of a smiling couple leaning close together, toasting with glasses of white wine outdoors"></div>

  <section class="panel body">
    <svg class="facets" viewBox="0 0 1200 1180" preserveAspectRatio="none" aria-hidden="true">
      <polygon points="0,0 520,0 0,560" fill="var(--pink-light)" opacity="0.3"/>
      <polygon points="0,560 300,1180 0,1180" fill="var(--pink-dark)" opacity="0.4"/>
      <polygon points="1200,0 1200,700 760,0" fill="var(--pink-dark)" opacity="0.35"/>
      <polygon points="700,1180 1200,700 1200,1180" fill="var(--pink-light)" opacity="0.25"/>
    </svg>
    <p class="body__intro">
      Some couples spend up big on their wedding day but fail<br>
      to invest in their marriage or relationship but relationships<br>
      take much more than love to be successful
    </p>
    <h2 class="body__question">
      <span class="body__question-lead">What</span>
      <span class="body__question-rest">you will gain from<br>Darren's seminar ?</span>
    </h2>
    <p class="body__pitch">
      This innovative one-day seminar<br>
      helps couples to breathe new life<br>
      into their relationship
    </p>
    <div class="presenter">
      <p class="presenter__label">presenter</p>
      <p class="presenter__name">Darren Whitfield</p>
      <p class="presenter__role">highly skilled couples therapist and educator</p>
    </div>
  </section>

  <div class="panel stripe stripe--bottom"><span class="blue"></span><span class="yellow"></span><span class="green"></span></div>

  <footer class="panel footer">
    <p class="footer__cta">Take your relationship to the next level and book your seat now</p>
    <p class="footer__url">http://www.darrenwhitfield.com.au/couples.html</p>
  </footer>

</main>
</body>
</html>
```